Online Psychology Practice needs business cards.

Online Psychology service needs business cards. Have own logo- please see uploaded. I have other file formats if you need (not sure one needed?)

Details for Business Card:
Helena Marchetti
Clinical Psychologist BPsych, BPsych (Hons), MPsych (Clin), MAPS
T: 0439627015 | F: 08 73615204
E: hello@brightwatertelehealthcounselling.com.au
W: brightwatertelehealthcounselling.com.au

Industry/Entity Type

Health

Contact Information for Business Card

Logo plus details above (couldn't write in this section)

```html
<!DOCTYPE html>
<html lang="en">
<head>
<meta charset="utf-8">
<title>Brightwater Telehealth Counselling – Business Cards</title>
<link rel="stylesheet" href="https://fonts.googleapis.com/css2?family=Arimo:wght@400;700&display=swap">
<style>
  :root {
    --backdrop: #e4e4e2;
    --card-blue: #175c86;
    --card-edge: #1a8cae;
    --pattern-dark: #134c70;
    --pattern-light: #3f8fc8;
    --name-teal: #2a9bbd;
    --text-white: #ffffff;
    --rule: #8fb6cf;
  }
  * { box-sizing: border-box; margin: 0; padding: 0; }
  html, body {
    width: 1200px; height: 801px; overflow: hidden;
    background: var(--backdrop);
    font-family: "Arimo", Arial, sans-serif;
  }
  .canvas { position: relative; width: 1200px; height: 801px; }
  .card {
    position: absolute;
    width: 620px; height: 354px;
    background: var(--card-blue);
    border-bottom: 3px solid var(--card-edge);
    overflow: hidden;
  }
  .card--details { left: 80px; top: 50px; }
  .card--brand { left: 500px; top: 412px; }

  /* Details side */
  .brand-block {
    position: absolute; left: 40px; top: 0; width: 230px; height: 100%;
    display: flex; align-items: center; gap: 12px;
  }
  .brand-dot {
    flex: none; width: 18px; height: 18px; border-radius: 50%;
    background: var(--text-white);
  }
  .brand-name {
    color: var(--text-white); font-weight: 700;
    font-size: 19px; line-height: 1.2; letter-spacing: 0.5px;
    text-transform: uppercase;
  }
  .divider {
    position: absolute; left: 290px; top: 90px; width: 1px; height: 190px;
    background: var(--rule);
  }
  .contact {
    position: absolute; left: 312px; top: 92px; width: 300px;
    color: var(--text-white); font-size: 12.5px; line-height: 1.45;
  }
  .contact__name {
    color: var(--name-teal); font-weight: 700; font-size: 19px;
    margin-bottom: 4px;
  }
  .contact__role { margin-bottom: 14px; }
  .contact__list { list-style: none; }
  .contact__item { display: flex; align-items: center; gap: 8px; white-space: nowrap; }
  .contact__icon { flex: none; width: 12px; height: 12px; fill: var(--text-white); }

  /* Brand side */
  .pattern-field {
    position: absolute; inset: 0;
    background: linear-gradient(120deg, var(--pattern-dark) 0%, var(--card-blue) 50%, var(--pattern-light) 100%);
  }
  .brand-lockup {
    position: absolute; right: 60px; top: 130px;
    display: flex; align-items: center; gap: 14px;
  }
  .brand-lockup .brand-name { font-size: 24px; }
</style>
</head>
<body>
<main class="canvas">

  <section class="card card--details" aria-label="Business card, contact side">
    <div class="brand-block">
      <span class="brand-dot" aria-hidden="true"></span>
      <p class="brand-name">Brightwater<br>Telehealth<br>Counselling</p>
    </div>
    <div class="divider" aria-hidden="true"></div>
    <div class="contact">
      <h1 class="contact__name">Helena Marchetti</h1>
      <p class="contact__role">Clinical Psychologist BPsych<br>BPsych (Hons), MPsych (Clin), MAPS</p>
      <ul class="contact__list">
        <li class="contact__item">
          <svg class="contact__icon" viewBox="0 0 24 24" aria-hidden="true"><path d="M6.6 10.8a15.1 15.1 0 0 0 6.6 6.6l2.2-2.2a1 1 0 0 1 1-.25 11.4 11.4 0 0 0 3.6.57 1 1 0 0 1 1 1V20a1 1 0 0 1-1 1A17 17 0 0 1 3 4a1 1 0 0 1 1-1h3.5a1 1 0 0 1 1 1c0 1.25.2 2.45.57 3.57a1 1 0 0 1-.25 1z"/></svg>
          0439627015
        </li>
        <li class="contact__item">
          <svg class="contact__icon" viewBox="0 0 24 24" aria-hidden="true"><path d="M6 2h10v6H6zM3 9h18v11H3zm4 3v2h2v-2zm4 0v2h2v-2zm4 0v2h2v-2zm-8 4v2h2v-2zm4 0v2h2v-2z"/></svg>
          08 73615204
        </li>
        <li class="contact__item">
          <svg class="contact__icon" viewBox="0 0 24 24" aria-hidden="true"><path d="M2 5h20v14H2zm2 2v.5l8 5 8-5V7l-8 5z"/></svg>
          hello@brightwatertelehealthcounselling.com.au
        </li>
        <li class="contact__item">
          <svg class="contact__icon" viewBox="0 0 24 24" aria-hidden="true"><path d="M12 2a10 10 0 1 0 0 20 10 10 0 0 0 0-20zm0 2c1 0 2.3 2 2.8 5H9.2C9.7 6 11 4 12 4zM4.3 11h4.8a20 20 0 0 0 0 2H4.3a8 8 0 0 1 0-2zm10.6 0h4.8a8 8 0 0 1 0 2h-4.8a20 20 0 0 0 0-2zM9.2 15h5.6c-.5 3-1.8 5-2.8 5s-2.3-2-2.8-5z"/></svg>
          brightwatertelehealthcounselling.com.au
        </li>
      </ul>
    </div>
  </section>

  <section class="card card--brand" aria-label="Business card, brand side">
    <div class="pattern-field" role="img" aria-label="Embossed repeating floral pattern in dark and light blue tones"></div>
    <div class="brand-lockup">
      <span class="brand-dot" aria-hidden="true"></span>
      <p class="brand-name">Brightwater<br>Telehealth<br>Counselling</p>
    </div>
  </section>

</main>
</body>
</html>
```